Brexmoor Solutions
Not Necessary
Simple
Marlon Teague
N/A
marlon@brexmoorsolutions.example
http://www.brexmoorsolutions.example
Brexmoor Solutions is a custom development/software development firm. Specialize on web and mobile development.
I'd be interested in what a double sided business card looks like but may settle on a one-sided card.
Your discretion on whether to use logo's font or another - whatever looks best.
Logo and fonts

```html
<!DOCTYPE html>
<html lang="en">
<head>
<meta charset="utf-8">
<title>Brexmoor Solutions – Business Card</title>
<link href="https://fonts.googleapis.com/css2?family=Open+Sans:wght@400;600;700&display=swap" rel="stylesheet">
<style>
  :root {
    --stage: #2b2d31;
    --white: #ffffff;
    --paper: #f4f5f7;
    --blue-deep: #0d3a66;
    --blue-mid: #1b5f9c;
    --blue-light: #3d8fd0;
    --logo-blue: #1f5f99;
    --text-light: #e6eef7;
    --text-muted: #b7cbe0;
  }
  * { margin: 0; padding: 0; box-sizing: border-box; }
  html, body { width: 1200px; height: 901px; overflow: hidden; }
  body {
    background: var(--stage);
    font-family: "Open Sans", Arial, sans-serif;
    display: flex;
    align-items: center;
    justify-content: center;
    gap: 50px;
  }
  .card {
    width: 525px;
    height: 300px;
    border-radius: 16px;
    overflow: hidden;
    position: relative;
    box-shadow: 0 14px 30px rgba(0,0,0,0.45);
  }

  /* Back side */
  .card-back {
    background: radial-gradient(ellipse at 35% 40%, var(--blue-light) 0%, var(--blue-mid) 40%, var(--blue-deep) 100%);
    display: flex;
    flex-direction: column;
    align-items: center;
    justify-content: center;
    color: var(--white);
  }
  .card-back .wordmark { color: var(--white); }
  .card-back .website {
    margin-top: 14px;
    font-size: 13px;
    letter-spacing: 1.5px;
    color: var(--text-light);
  }

  /* Wordmark (name set in plain text) */
  .wordmark {
    font-weight: 400;
    text-align: center;
    line-height: 1;
    color: var(--logo-blue);
  }
  .wordmark .name { display: block; font-size: 52px; letter-spacing: 0.5px; }
  .wordmark .tag { display: block; font-size: 19px; letter-spacing: 6px; margin-top: 4px; }

  /* Front side */
  .card-front { display: flex; background: var(--paper); }
  .front-logo {
    width: 46%;
    background: linear-gradient(180deg, var(--white) 0%, var(--paper) 100%);
    display: flex;
    align-items: center;
    justify-content: center;
    box-shadow: 4px 0 10px rgba(0,0,0,0.25);
    z-index: 1;
  }
  .front-logo .wordmark .name { font-size: 40px; }
  .front-logo .wordmark .tag { font-size: 15px; letter-spacing: 5px; }
  .front-info {
    flex: 1;
    background: radial-gradient(ellipse at 30% 35%, var(--blue-light) 0%, var(--blue-mid) 45%, var(--blue-deep) 100%);
    color: var(--text-light);
    padding: 24px 24px 0 26px;
    position: relative;
  }
  .person-name { font-size: 15px; font-weight: 700; color: var(--white); }
  .person-title { position: absolute; top: 128px; left: 26px; font-size: 11px; color: var(--text-muted); }
  .contact-list {
    position: absolute;
    left: 26px;
    bottom: 26px;
    list-style: none;
    font-size: 12px;
  }
  .contact-list li { display: flex; align-items: center; gap: 8px; margin-top: 6px; white-space: nowrap; }
  .contact-list svg { width: 12px; height: 12px; flex: none; fill: none; stroke: var(--text-light); stroke-width: 1.4; }
</style>
</head>
<body>

  <section class="card card-back" aria-label="Card back">
    <div class="wordmark">
      <span class="name">Brexmoor</span>
      <span class="tag">SOLUTIONS</span>
    </div>
    <p class="website">www.brexmoorsolutions.example</p>
  </section>

  <section class="card card-front" aria-label="Card front">
    <div class="front-logo">
      <div class="wordmark">
        <span class="name">Brexmoor</span>
        <span class="tag">SOLUTIONS</span>
      </div>
    </div>
    <div class="front-info">
      <h1 class="person-name">Marlon Teague</h1>
      <p class="person-title">N/A</p>
      <ul class="contact-list">
        <li>
          <svg viewBox="0 0 12 12" aria-hidden="true"><rect x="3" y="1" width="6" height="10" rx="1"/><line x1="5" y1="9" x2="7" y2="9"/></svg>
          555-013-7482
        </li>
        <li>
          <svg viewBox="0 0 12 12" aria-hidden="true"><rect x="1" y="2.5" width="10" height="7"/><polyline points="1,2.5 6,6.5 11,2.5"/></svg>
          marlon@brexmoorsolutions.example
        </li>
        <li>
          <svg viewBox="0 0 12 12" aria-hidden="true"><circle cx="6" cy="6" r="5"/><ellipse cx="6" cy="6" rx="2.2" ry="5"/><line x1="1" y1="6" x2="11" y2="6"/></svg>
          www.brexmoorsolutions.example
        </li>
      </ul>
    </div>
  </section>

</body>
</html>
```